Start up in business consultancy needs a business card

We need the business card's layout (we have already the logo). Our business is concerned on consultancy services delivered to companies on the matter of sustainability. Business card should be enough essentials and professional style.

Side A with the following info:
logo + a space for the claim (still to identify) + website of the company

Side B with the following info:
Name of business card holder + title of the business card holder + address of the company + space for mobile number, phone number, fax number + e-mail of business card holder + graphic details around.

Target Market(s)

Business of any sector

Industry/Entity Type

Business Service

Contact Information for Business Card

Name of the company:
Pianoverde srl
Società Benefit

Address of the company:
Via Lucerna, 7
21047 - Saronno (VA)

Website:
www.pianoverde.it

Name of the BC' holder:
Luca Ferentino

Title:
Co-fondatore

Email:
luca@pianoverde.it

Mobile:
+39 348 915 2074
Phone:
+39 348 915 2074
Fax:
+39 348 915 2074

Font styles to use
Other font styles liked:
• new gothic

```html
<!DOCTYPE html>
<html lang="it">
<head>
<meta charset="utf-8">
<title>Pianoverde – biglietto da visita</title>
<link rel="stylesheet" href="https://fonts.googleapis.com/css2?family=Outfit:wght@300;400;500;600&display=swap">
<style>
  :root {
    --brand-blue: #1866ad;
    --paper: #ffffff;
    --backdrop: #5a5a5a;
    --shadow: rgba(0, 0, 0, 0.45);
  }
  * { margin: 0; padding: 0; box-sizing: border-box; }
  html, body {
    width: 1200px; height: 1200px; overflow: hidden;
    background: var(--backdrop);
    font-family: "Outfit", "Century Gothic", sans-serif;
  }
  .stage { position: relative; width: 1200px; height: 1200px; }
  .card {
    position: absolute; left: 254px; width: 692px; height: 392px;
    box-shadow: 4px 6px 12px var(--shadow);
  }
  .card--front { top: 143px; background: var(--brand-blue); color: var(--paper); }
  .card--back  { top: 664px; background: var(--paper); color: var(--brand-blue); }

  .brand { position: absolute; display: flex; align-items: center; }
  .brand__dot { border-radius: 50%; border-style: solid; border-color: currentColor; }
  .brand__name { font-weight: 500; letter-spacing: 0.5px; line-height: 1; }

  .card--front .brand { left: 114px; top: 94px; gap: 22px; }
  .card--front .brand__dot { width: 140px; height: 140px; border-width: 7px; }
  .card--front .brand__name { font-size: 50px; }

  .website {
    position: absolute; left: 0; right: 0; top: 339px;
    text-align: center; font-size: 17px; font-weight: 300;
  }

  .card--back .brand { left: 40px; top: 148px; gap: 18px; }
  .card--back .brand__dot { width: 104px; height: 104px; border-width: 5px; }
  .card--back .brand__name { font-size: 38px; }

  .holder { position: absolute; right: 34px; top: 38px; text-align: right; }
  .holder__name { font-size: 25px; font-weight: 600; line-height: 1.1; }
  .holder__title { font-size: 17px; font-weight: 300; margin-top: 2px; }

  .contacts { position: absolute; right: 34px; top: 182px; list-style: none; }
  .contacts li {
    display: flex; justify-content: flex-end; align-items: center; gap: 7px;
    height: 23px; font-size: 18px; font-weight: 300;
  }
  .contacts svg { width: 18px; height: 18px; fill: none; stroke: currentColor; stroke-width: 1.6; }
  .contacts svg .solid { fill: currentColor; stroke: none; }

  .address {
    position: absolute; right: 34px; top: 316px; text-align: right;
    font-size: 18px; font-weight: 300; line-height: 23px;
  }
</style>
</head>
<body>
<main class="stage">

  <section class="card card--front" aria-label="Fronte">
    <div class="brand">
      <span class="brand__dot" aria-hidden="true"></span>
      <span class="brand__name">pianoverde</span>
    </div>
    <p class="website">www.pianoverde.it</p>
  </section>

  <section class="card card--back" aria-label="Retro">
    <div class="brand">
      <span class="brand__dot" aria-hidden="true"></span>
      <span class="brand__name">pianoverde</span>
    </div>

    <div class="holder">
      <p class="holder__name">Luca Ferentino</p>
      <p class="holder__title">Co-fondatore</p>
    </div>

    <ul class="contacts">
      <li>+39 348 915 2074
        <svg viewBox="0 0 18 18" aria-label="cellulare"><rect x="4.5" y="1.5" width="9" height="15" rx="1.5"/><line x1="7.5" y1="14" x2="10.5" y2="14"/></svg>
      </li>
      <li>+39 348 915 2074
        <svg viewBox="0 0 18 18" aria-label="telefono"><path class="solid" d="M1 6c0-2 3-3.5 8-3.5S17 4 17 6v1.5h-4V5.5H5v2H1z"/><path class="solid" d="M4 9l2-2.5h6L14 9v6H4z"/><circle cx="9" cy="11.5" r="1.6" fill="#fff" stroke="none"/></svg>
      </li>
      <li>+39 348 915 2074
        <svg viewBox="0 0 18 18" aria-label="fax"><path class="solid" d="M5 1.5h8v4H5z"/><path class="solid" d="M2 6.5h14v7h-2.5v-2.5h-9v2.5H2z"/><path class="solid" d="M5.5 12h7v4.5h-7z"/></svg>
      </li>
      <li>luca@pianoverde.it
        <svg viewBox="0 0 18 18" aria-label="email"><rect class="solid" x="1" y="3.5" width="16" height="11"/><path d="M1.5 4l7.5 6 7.5-6M1.5 14l5.5-5M16.5 14l-5.5-5" stroke="#fff" stroke-width="1.3"/></svg>
      </li>
      <li>www.pianoverde.it
        <svg viewBox="0 0 18 18" aria-label="sito web"><circle cx="9" cy="9" r="7.5"/><ellipse cx="9" cy="9" rx="3.3" ry="7.5"/><line x1="1.5" y1="9" x2="16.5" y2="9"/><path d="M3 5h12M3 13h12"/></svg>
      </li>
    </ul>

    <address class="address" style="font-style:normal">
      Via Lucerna, 7<br>
      21047 - Saronno (VA)
    </address>
  </section>

</main>
</body>
</html>
```